New Infographic Design Project

I need a 1 page Infographic that explains our Quillstone Prism offer.

Can you use the following content in the attached document to create a 1 page infographic. The image in the bottom of the document is one of our competitors who is offering the same thing, this image is only provided for inspiration and ideas as we need ours to be based on the content of the document and aligned with the Corvenly Brand

```html
<!DOCTYPE html>
<html lang="en">
<head>
<meta charset="utf-8">
<title>Corvenly – Data Ready. AI Ready. In 6 Weeks.</title>
<link href="https://fonts.googleapis.com/css2?family=Montserrat:wght@300;400;500;600;700;800&display=swap" rel="stylesheet">
<style>
:root{
  --navy:#021d6b;
  --navy-ink:#0b1f63;
  --red:#d81f2a;
  --teal:#00c8a6;
  --white:#ffffff;
  --grey-text:#5d6170;
  --body-text:#2a2d3a;
  --card-top:#e3e5ee;
  --panel-top:#e2e4ec;
}
*{box-sizing:border-box;margin:0;padding:0}
html,body{width:1200px;height:675px;overflow:hidden;background:var(--white)}
body{font-family:"Montserrat",sans-serif;position:relative;color:var(--navy-ink)}
.abs{position:absolute}

/* header */
.headline{left:36px;top:22px;font-size:27.5px;font-weight:800;line-height:30px;color:var(--navy)}
.headline span{color:var(--red)}
.brace{left:228px;top:20px}
.partner-title{left:277px;top:19px;font-size:24px;font-weight:500;color:var(--navy)}
.partner-copy{left:280px;top:48px;width:745px;font-size:12.7px;line-height:15.7px;color:var(--body-text)}
.partner-copy em{font-style:normal;color:var(--red)}
.brand{left:1060px;top:52px;font-size:24px;font-weight:600;color:var(--navy)}

/* navy band */
.band{left:0;top:128px;width:1200px;height:547px;background:var(--navy)}
.edge-title{left:0;top:142px;width:1200px;text-align:center;font-size:17px;font-weight:400;letter-spacing:14.5px;color:var(--white)}
.offer{left:1056px;top:148px;width:112px;height:26px;background:var(--white);border-radius:5px;padding:4px 7px;color:var(--navy-ink);line-height:9px}
.offer small{display:block;font-size:6.5px;font-weight:500}
.offer b{display:block;font-size:8.6px;font-weight:500;margin-top:1px}
.powered{left:1057px;top:183px;display:flex;align-items:center;gap:5px;color:var(--white)}
.powered small{font-size:6px;letter-spacing:.3px}
.powered i{display:block;width:15px;height:15px;background:#f0f2f8}
.powered b{font-size:9.5px;font-weight:600}

.edge-col{border-left:1px dashed rgba(255,255,255,.75);border-bottom:1px dashed rgba(255,255,255,.75);border-bottom-left-radius:4px}
.edge-col::before{content:"";position:absolute;left:-4px;top:-6px;width:7px;height:7px;border:1.5px solid var(--white);border-radius:50%;background:var(--navy)}
.edge-col h3{position:absolute;left:18px;top:2px;font-size:16.3px;font-weight:400;line-height:19px;color:var(--white)}
.edge-col p{position:absolute;left:19px;font-size:11px;line-height:15.7px;color:var(--white)}
.edge-col svg{position:absolute}

/* timeline */
.teal{left:0;top:339px;width:1200px;height:141px;background:var(--teal)}
.six{left:30px;top:352px;font-size:58px;font-weight:400;color:var(--white);line-height:60px}
.week-word{left:33px;top:400px;font-size:27px;font-weight:400;color:var(--white)}
.ttv{left:31px;top:439px;font-size:12px;color:var(--white)}
.track{left:32px;top:433px;width:1140px;height:1.5px;background:var(--white)}
.card{top:327px;width:162px;height:170px;border-radius:9px;background:linear-gradient(180deg,var(--card-top) 0%,var(--white) 32%)}
.card .dot{position:absolute;left:-3px;top:103px;width:6px;height:6px;border-radius:50%;background:var(--red)}
.card .tag{position:absolute;left:13px;top:-6px;background:var(--red);color:var(--white);font-size:7.8px;font-weight:600;padding:2px 4px;border-radius:3px}
.card h4{position:absolute;left:14px;top:20px;font-size:10.3px;font-weight:600;line-height:11px;color:var(--navy-ink)}
.card p{position:absolute;left:11px;top:54px;width:146px;font-size:9.4px;line-height:15.6px;color:var(--grey-text)}

/* extra edge */
.panel{left:37px;top:533px;width:1123px;height:128px;border-radius:10px;background:linear-gradient(180deg,var(--panel-top),#f7f8fb)}
.extra{left:72px;top:580px;font-size:13px;color:var(--red)}
.edge-big{left:70px;top:592px;font-size:28px;font-weight:300;color:var(--navy-ink)}
.extra-col h5{font-size:14px;font-weight:600;color:var(--navy-ink);white-space:nowrap;display:flex;align-items:center;gap:6px}
.extra-col p{margin-top:14px;font-size:10.3px;line-height:15.7px;color:var(--grey-text)}
.divider{top:560px;height:75px;border-left:1px dotted #8a8fa3}
</style>
</head>
<body>

<header>
  <h1 class="abs headline">Data Ready<span>.</span><br>AI Ready<span>.</span><br>In 6 Weeks<span>.</span></h1>
  <svg class="abs brace" width="16" height="96" viewBox="0 0 16 96" aria-hidden="true">
    <path d="M3 2 C10 2 9 10 9 20 L9 38 C9 44 11 47 14 48 C11 49 9 52 9 58 L9 76 C9 86 10 94 3 94" fill="none" stroke="var(--red)" stroke-width="2"/>
  </svg>
  <h2 class="abs partner-title">Your long-term strategic data partner</h2>
  <p class="abs partner-copy">We start with a <em>Business Data Assessment</em> or <em>Prism Deployment Assessment</em> to pinpoint the highest-value use cases,the biggest data risks, and the fastest path to impact. We stand up a governed <em>Quillstone Prism</em> foundation using&nbsp; repeatable ingestion, validation, and common data model patterns, so your reporting scales cleanly and your AI initiatives provide business value.</p>
  <div class="abs brand">Corvenly</div>
</header>

<section class="abs band"></section>
<h2 class="abs edge-title">THE CORVENLY EDGE</h2>
<div class="abs offer"><small>FULLY FUNDED FOR A</small><b>LIMITED TIME OFFER</b></div>
<div class="abs powered"><small>POWERED BY</small><i></i><b>Halvera</b></div>

<div class="abs edge-col" style="left:158px;top:187px;width:197px;height:108px">
  <h3>Quality-first<br>delivery</h3>
  <p style="top:45px;width:178px">Automated validation, data tests, and “quality gates” that stop bad data upstream.</p>
  <svg style="left:176px;top:0" width="20" height="20" viewBox="0 0 20 20" aria-hidden="true"><circle cx="10" cy="10" r="9" fill="var(--white)"/><path d="M6 10l3 3 5-6" stroke="var(--red)" stroke-width="2.2" fill="none"/></svg>
</div>
<div class="abs edge-col" style="left:370px;top:187px;width:210px;height:119px">
  <h3>Data products,<br>not datasets</h3>
  <p style="top:46px;width:195px">Clear ownership, SLAs, versioning, and reusable, consumable outputs aligned to high impact business outcomes.</p>
  <svg style="left:186px;top:0" width="20" height="20" viewBox="0 0 20 20" aria-hidden="true"><path d="M10 1l8 4.5-8 4.5-8-4.5z" fill="var(--white)"/><path d="M2 5.5v9l8 4.5v-9z" fill="#e8e8ee"/><path d="M18 5.5v9l-8 4.5v-9z" fill="var(--red)"/></svg>
</div>
<div class="abs edge-col" style="left:599px;top:187px;width:264px;height:87px">
  <h3>Governance that doesn’t<br>slow you down</h3>
  <p style="top:43px;width:240px">Security, access, lineage, and auditability built in from day one.</p>
  <svg style="left:248px;top:0" width="20" height="20" viewBox="0 0 20 20" aria-hidden="true"><circle cx="10" cy="10" r="8" fill="none" stroke="var(--white)" stroke-width="1.8"/><path d="M11 2L6 11h4l-1 7 5-9h-4z" fill="var(--red)"/></svg>
</div>
<div class="abs edge-col" style="left:887px;top:187px;width:145px;height:104px">
  <h3>Operate<br>seamlessly</h3>
  <p style="top:45px;width:140px">CI/CD, monitoring, and cost controls so the platform stays healthy.</p>
  <svg style="left:120px;top:2px" width="24" height="16" viewBox="0 0 24 16" aria-hidden="true"><circle cx="7" cy="8" r="5" fill="none" stroke="var(--white)" stroke-width="2.5"/><circle cx="17" cy="8" r="5" fill="none" stroke="var(--red)" stroke-width="2.5"/></svg>
</div>

<section class="abs teal"></section>
<div class="abs track"></div>
<div class="abs six">6</div>
<div class="abs week-word">week</div>
<div class="abs ttv">time to value</div>

<article class="abs card" style="left:120px"><span class="dot"></span><span class="tag">WEEK 1</span>
  <h4>Envision &amp; Assess</h4>
  <p>Use case shortlist and priority based on highest business impact, current-state review, data risk &amp; compliance priorities, target operating model.</p></article>
<article class="abs card" style="left:296px"><span class="dot"></span><span class="tag">WEEK 2</span>
  <h4>Architecture &amp;<br>Governance Design</h4>
  <p>Landing zone decisions, security and access model, patterns/standards, delivery plan and success metrics.</p></article>
<article class="abs card" style="left:473px"><span class="dot"></span><span class="tag">WEEK 3</span>
  <h4>Prism Foundation<br>Deployed</h4>
  <p>Workspaces and environments, automation &amp; CI/CD, onboarding playbooks, baseline policies /guardrails.</p></article>
<article class="abs card" style="left:649px"><span class="dot"></span><span class="tag">WEEK 4</span>
  <h4>Data ingestion +<br>Validation Framework</h4>
  <p>Reusable ingestion patterns, automated validation, data contracts/SLAs, observability signals and alerting.</p></article>
<article class="abs card" style="left:826px"><span class="dot"></span><span class="tag">WEEK 5</span>
  <h4>Scalable Common<br>Data Model</h4>
  <p>Domain model, master entities, curated layer, semantic modelling patterns that support Brightlens BI at scale.</p></article>
<article class="abs card" style="left:1003px"><span class="dot"></span><span class="tag">WEEK 6</span>
  <h4>Business outcomes +<br>AI-ready capability</h4>
  <p>Executive dashboards and priority reports, performance optimisation, hypercare and handover, AI readiness check and pilot plan (predictive analytics and/or secure enterprise LLM).</p></article>

<section class="abs panel"></section>
<div class="abs extra">EXTRA</div>
<div class="abs edge-big">EDGE</div>
<div class="abs extra-col" style="left:167px;top:556px"><h5>“AI-ready data” guarantee <svg width="9" height="9" viewBox="0 0 9 9" aria-hidden="true"><path d="M1 8L8 1M3 1h5v5" fill="none" stroke="var(--red)" stroke-width="1.4"/></svg></h5>
  <p style="width:205px">Every priority dataset ships with validation rules, ownership, lineage, and freshness SLAs before it can power AI.</p></div>
<div class="abs divider" style="left:396px"></div>
<div class="abs extra-col" style="left:420px;top:555px"><h5>Cost-to-serve transparency <svg width="9" height="9" viewBox="0 0 9 9" aria-hidden="true"><path d="M1 8L8 1M3 1h5v5" fill="none" stroke="var(--red)" stroke-width="1.4"/></svg></h5>
  <p style="width:168px">Show business owners what each product/report costs to run and optimise it continuously.</p></div>
<div class="abs divider" style="left:644px"></div>
<div class="abs extra-col" style="left:670px;top:555px"><h5>Change-proof pipelines <svg width="9" height="9" viewBox="0 0 9 9" aria-hidden="true"><path d="M1 8L8 1M3 1h5v5" fill="none" stroke="var(--red)" stroke-width="1.4"/></svg></h5>
  <p style="width:215px">Data contracts + automated tests reduce breakages from upstream schema changes.</p></div>
<div class="abs divider" style="left:904px"></div>
<div class="abs extra-col" style="left:927px;top:557px"><h5>Governed self-serve <svg width="9" height="9" viewBox="0 0 9 9" aria-hidden="true"><path d="M1 8L8 1M3 1h5v5" fill="none" stroke="var(--red)" stroke-width="1.4"/></svg></h5>
  <p style="width:205px">Catalog + certified datasets so teams move faster without creating data chaos.</p></div>

</body>
</html>
```